Gift Cards in the Mail Envelope

Mailing out gift cards in the envelope. Need an eye popping envelope. Please look at the enclosed images. The envelope should look like that.

Low design quality

```html
<!DOCTYPE html>
<html lang="en">
<head>
<meta charset="utf-8">
<title>Gift Card Envelope Template</title>
<link rel="stylesheet" href="https://fonts.googleapis.com/css2?family=Archivo+Black&family=Figtree:wght@600&family=Nunito+Sans:wght@300;700&display=swap">
<style>
  :root {
    --paper: #ffffff;
    --envelope-pink: #f7d4d8;
    --fold-line: #f0b6bd;
    --ribbon-red: #88232b;
    --faint-text: #f2c8ce;
    --ink: #222222;
    --instruction-ink: #3a3a3a;
  }
  html, body {
    margin: 0;
    padding: 0;
    width: 1200px;
    height: 849px;
    overflow: hidden;
    background: var(--paper);
  }
  .template {
    display: block;
    width: 1200px;
    height: 849px;
  }
  .panel { fill: var(--envelope-pink); stroke: var(--fold-line); stroke-width: 3; }
  .closing-flap { fill: var(--ribbon-red); }
  .instructions-title { font-family: "Nunito Sans", sans-serif; font-weight: 700; font-size: 30px; fill: var(--ink); }
  .instructions-step { font-family: "Nunito Sans", sans-serif; font-weight: 300; font-size: 30px; letter-spacing: 1.5px; fill: var(--instruction-ink); }
  .greeting { font-family: "Archivo Black", sans-serif; font-size: 122px; fill: var(--ribbon-red); letter-spacing: 2px; }
  .back-word { font-family: "Figtree", sans-serif; font-weight: 600; font-size: 335px; fill: var(--faint-text); }
</style>
</head>
<body>
<svg class="template" viewBox="0 0 2339 1654" xmlns="http://www.w3.org/2000/svg">
  <defs>
    <linearGradient id="gift-tones" x1="0" y1="0" x2="1" y2="1">
      <stop offset="0" stop-color="#d98f98"/>
      <stop offset="0.55" stop-color="#e9a2aa"/>
      <stop offset="1" stop-color="#88232b"/>
    </linearGradient>
  </defs>

  <g class="instructions">
    <text class="instructions-title" x="40" y="55">Simple Envelop Design</text>
    <text class="instructions-step" x="40" y="91">1. Cut the template from the paper</text>
    <text class="instructions-step" x="40" y="127">2. Fold along the lines</text>
    <text class="instructions-step" x="40" y="164">3. Use adhesive or tape to fasten the edges.</text>
    <text class="instructions-step" x="40" y="200">(can de adjusted to preference size)</text>
  </g>

  <g class="envelope">
    <polygon class="panel top-flap" points="931,250 984,54 1744,54 1786,250"/>
    <polygon class="panel bottom-flap" points="931,1375 984,1570 1744,1570 1786,1375"/>
    <rect class="panel back-panel" x="195" y="250" width="736" height="1125"/>
    <rect class="panel front-panel" x="931" y="250" width="855" height="1125"/>
    <polygon class="closing-flap" points="1786,250 2140,291 2140,1328 1786,1375"/>

    <text class="back-word" transform="translate(835,1293) rotate(-90)" textLength="988" lengthAdjust="spacingAndGlyphs">ENJOY</text>

    <rect class="gift-illustration" x="1005" y="250" width="736" height="570" fill="url(#gift-tones)" role="img" aria-label="Illustration of a pink wrapped gift box tied with a dark red ribbon and bow"/>

    <text class="greeting" transform="translate(1150,1315) rotate(90)" text-anchor="end">A GIFT</text>
    <text class="greeting" transform="translate(987,1310) rotate(90)" text-anchor="end">FOR YOU!</text>
  </g>
</svg>
</body>
</html>
```